E-commerce portal dedicated for selling books

We are looking for a design of a professional and official e-commerce web-site for a new company that is specialized in selling books (both books formats, printed and electronic), we’ll deal also with used-books where we plan to buy used books and re-sell them to other clients, or let the clients can sell their used-books directly to another client,
Web site must be very clear for users who like to brows the site contents or to buy a book, we will make the books available in discounted prices.
Customer should be able to perform the following actions in the site:
Search the book he/she is looking for easily
Get a brief description and details about the author, publisher, book content, browse the book’s content, browse first 20 pages ,
View similar or related books and a list of books that other users who bought this books also bought
Read and write reviews
Sign-up in the site
Complete the purchase process
Users can also sell or buy used-books from the site.
Look and feel:
The site’s look and feel is preferred to be clean, simple and balanced
Web site design is preferred to be simple with no strong or dark colors
User should feel comfort when looking at the home page because the design simplicity and comfortable colors
I liked the following sites’ look and feel:
http://www.qirtas.ae/
http://www.velmora.com/
http://www.tulvinghart.com/
Please be sure to include all common elements that are used in the e-commerce web sites like Search, online form(s), shopping cart / ordering, user log in/member, printer-friendly function, subscription to newsletter.....

```html
<!DOCTYPE html>
<html lang="en">
<head>
<meta charset="utf-8">
<title>Book Store Home</title>
<link href="https://fonts.googleapis.com/css2?family=Arimo:wght@400;700&family=Open+Sans:wght@400;600&display=swap" rel="stylesheet">
<style>
:root{
  --ink:#111;
  --black:#000;
  --white:#fff;
  --grey-line:#c9c9c9;
  --grey-soft:#e6e6e6;
  --grey-panel:#ececec;
  --grey-mid:#8a8a8a;
  --grey-dark:#555;
  --sale:#c0141b;
  --link:#3a2a7a;
  --select:#6b6b6b;
}
*{box-sizing:border-box;margin:0;padding:0}
html,body{width:1200px;height:1000px;overflow:hidden;background:var(--white)}
body{position:relative;font-family:"Arimo",Arial,sans-serif;color:var(--ink)}
.abs{position:absolute}

/* header */
.site-header{left:347px;top:0;width:506px;height:55px;background:var(--black);color:var(--white)}
.logo{left:50px;top:6px;font-size:21px;font-weight:700;letter-spacing:.5px}
.top-links{right:50px;top:3px;font-size:5px;white-space:nowrap}
.perks{left:170px;top:16px;display:flex;gap:14px;font-size:5px;line-height:1.35}
.perk{display:flex;gap:4px;align-items:flex-start}
.perk b{display:block;font-weight:700}
.perk svg{width:11px;height:11px;flex:none}

/* categories */
.categories{left:397px;top:38px;width:93px;height:232px;background:var(--white);border:1px solid var(--grey-line);box-shadow:1px 1px 3px rgba(0,0,0,.25)}
.categories-head{height:15px;background:var(--black);color:var(--white);font-size:6px;padding:4px 4px;position:relative}
.categories-head i{position:absolute;right:2px;top:2px;width:13px;height:11px;background:var(--grey-mid)}
.categories ul{list-style:none;padding-top:7px}
.categories li{font-size:5.6px;height:15.3px;line-height:15.3px;padding-left:5px}
.categories li.is-active{background:var(--select);color:var(--white)}

/* search */
.search{left:498px;top:40px;height:12px;display:flex;gap:3px;font-size:5px}
.search .select{width:66px;border:1px solid var(--grey-line);color:var(--grey-mid);padding:3px 3px;background:var(--white)}
.search .field{width:126px;border:1px solid var(--grey-line);color:var(--grey-mid);padding:3px 3px;background:#f7f7ee}
.search .btn{width:38px;background:var(--black);color:var(--white);text-align:center;padding-top:3px}
.cart-btn{left:742px;top:40px;width:60px;height:12px;background:var(--black);color:var(--white);font-size:4.8px;padding:3px 3px 0 14px}
.cart-btn svg{position:absolute;left:3px;top:2px;width:8px;height:8px}

/* hero */
.hero{left:497px;top:53px;width:204px;height:165px;background:linear-gradient(#fafafa,#d6d6d6);border:1px solid var(--grey-line)}
.hero h2{position:absolute;left:19px;top:17px;width:150px;font-size:7px;line-height:1.5;font-weight:700;color:#444}
.hero .art{position:absolute;left:12px;top:60px;width:170px;height:100px;background:linear-gradient(90deg,#d84a7a,#3a8a66 45%,#2d6b3b 60%,#c7a46b);opacity:.85}
.arrow-btn{position:absolute;top:76px;width:12px;height:12px;background:var(--white);border:1px solid var(--grey-line)}
.arrow-btn svg{width:10px;height:10px}
.shop-now{position:absolute;background:var(--black);color:var(--white);font-size:4.5px;font-weight:700;padding:2px 3px}

.promo{background:linear-gradient(#f4f4f4,#cfcfcf);border:1px solid var(--grey-line)}
.promo .art{position:absolute}
.promo .strip{position:absolute;left:0;right:0;bottom:0;height:9px;background:#222;color:var(--white);font-size:4.5px;font-weight:700;padding:2px 3px;display:flex;justify-content:space-between}
.promo .strip span.btn{background:var(--black);border:1px solid #666;padding:0 2px}
.promo p{position:absolute;font-size:5.6px;font-weight:700;color:#333;line-height:1.45}
.badge{position:absolute;width:14px;height:14px;border-radius:50%;background:#d32027}

/* newsletter */
.newsletter{left:397px;top:308px;width:405px;height:18px;background:var(--grey-soft);border:1px solid var(--grey-line)}
.newsletter .label{position:absolute;left:0;top:0;height:16px;width:134px;background:var(--black);color:var(--white);font-size:5px;padding:5px 8px;clip-path:polygon(0 0,92% 0,100% 50%,92% 100%,0 100%)}
.newsletter .field{position:absolute;left:138px;top:3px;width:210px;height:10px;background:var(--white);border:1px solid var(--grey-line);font-size:4.8px;color:var(--grey-mid);padding:2px 3px}
.newsletter .btn{position:absolute;left:354px;top:2px;width:48px;height:12px;background:var(--black);color:var(--white);font-size:5.5px;text-align:center;padding-top:3px}

/* book sections */
.section-title{left:397px;width:405px;font-family:"Open Sans",Arial,sans-serif;font-size:9.5px;font-weight:600;border-bottom:1px solid var(--grey-line);padding-bottom:2px}
.section-title .view-all{position:absolute;right:0;top:3px;font-family:"Arimo",Arial,sans-serif;font-size:5.5px;font-weight:400}
.shelf{left:397px;display:flex;gap:7.5px}
.book{width:75px;height:118px;border:1px solid var(--grey-line);background:var(--white);position:relative}
.book.is-focus{box-shadow:0 0 0 1px #999,1px 1px 3px rgba(0,0,0,.4)}
.cover{width:44px;height:65px;margin:7px auto 0;border:1px solid #bbb}
.book .title{font-size:5px;text-align:center;margin-top:4px}
.book .price{display:flex;font-size:5px;padding:0 4px;margin-top:11px;gap:5px}
.book .price s{color:var(--grey-mid)}
.book .price b{font-weight:700}
.book .price em{font-style:normal;color:var(--sale);margin-left:auto}
.book .cod{position:absolute;left:2px;right:2px;bottom:2px;height:10px;border-top:1px solid var(--grey-line);font-size:4.5px;padding:3px 0 0 14px}
.book .cod svg{position:absolute;left:2px;top:1px;width:8px;height:8px}
.nav-circle{width:19px;height:19px;border-radius:50%;background:#bdbdbd}
.nav-circle svg{width:19px;height:19px}

/* publishers */
.publishers{left:397px;top:797px;width:405px;height:43px;background:linear-gradient(#fff,#ededed 50%,#fff);border-bottom:1px solid var(--grey-line);display:flex;align-items:center;justify-content:space-around;padding:0 22px}
.publisher{display:flex;align-items:center;gap:3px;font-size:6px;font-weight:700;color:#333}
.publisher i{width:8px;height:8px;border-radius:50%;background:#777;display:block}
.pub-arrow{position:absolute;top:14px;width:10px;height:14px}

/* footer */
.site-footer{left:347px;top:861px;width:506px;height:111px;background:var(--grey-panel);border-top:2px solid #d5d5d5}
.col{position:absolute;top:12px;font-size:4.8px;line-height:11px;color:#333}
.col h4{font-size:5.6px;font-weight:700;margin-bottom:1px}
.col .lnk{color:var(--link)}
.contact-row{position:relative;padding-left:12px}
.contact-row svg{position:absolute;left:0;top:2px;width:7px;height:7px}
.social{display:flex;gap:5px;margin-top:4px}
.social i{display:block;width:11px;height:11px;background:#3b6ea8}
.to-top{left:822px;top:936px;width:23px;height:23px;border-radius:50%;background:var(--black)}
.legal{left:347px;top:972px;width:506px;height:28px;background:var(--black);color:#ccc;font-size:4.5px}
.legal span{position:absolute;top:11px}
</style>
</head>
<body>

<header class="site-header abs">
  <div class="logo abs">LOGO</div>
  <div class="top-links abs">24x7 Customer Support &nbsp;·&nbsp; Contact Us &nbsp;|&nbsp; Home &nbsp;|&nbsp; My Account &nbsp;|&nbsp; Wishlist &nbsp;|&nbsp; Login &nbsp;|&nbsp; Signup</div>
  <div class="perks abs">
    <div class="perk"><svg viewBox="0 0 12 12"><path d="M2 1h3l1 3-2 1a7 7 0 0 0 3 3l1-2 3 1v3c-5 1-10-4-9-9z" fill="#fff"/></svg><span><b>CALL US</b>011 555 01420</span></div>
    <div class="perk"><svg viewBox="0 0 12 12"><rect x="1" y="3" width="10" height="6" rx="1" fill="#fff"/><circle cx="6" cy="6" r="1.6" fill="#000"/></svg><span><b>PAY ON DELIVERY</b>Pay cash at your doorstep</span></div>
    <div class="perk"><svg viewBox="0 0 12 12"><path d="M0 3h7v5H0zM7 5h3l2 2v1H7z" fill="#fff"/><circle cx="2.5" cy="9.5" r="1.3" fill="#fff"/><circle cx="9.5" cy="9.5" r="1.3" fill="#fff"/></svg><span><b>FREE SHIPPING</b>Nationwide</span></div>
    <div class="perk"><svg viewBox="0 0 12 12"><rect x="2" y="5" width="8" height="7" fill="#fff"/><path d="M4 5V3a2 2 0 0 1 4 0v2" stroke="#fff" fill="none" stroke-width="1.3"/></svg><span><b>SECURE WEBSITE</b>Encrypted connection</span></div>
  </div>
</header>

<nav class="categories abs">
  <div class="categories-head">All Categories<i></i></div>
  <ul>
    <li>Academic and Professional</li>
    <li>Biographies &amp; Autobiographies</li>
    <li>Investing and Management</li>
    <li>Coffee Table</li>
    <li>College Text &amp; Reference</li>
    <li>Comics &amp; Graphic Novels</li>
    <li>Computers &amp; Internet</li>
    <li>Entrance Exams Preparation</li>
    <li>Literature &amp; Fiction</li>
    <li class="is-active">Science &amp; Technology</li>
    <li>Teens</li>
    <li>Travel</li>
    <li>Other....</li>
  </ul>
</nav>

<form class="search abs">
  <div class="select">Category ▾</div>
  <div class="field">Search for your item...</div>
  <div class="btn">SEARCH</div>
</form>
<div class="cart-btn abs"><svg viewBox="0 0 10 10"><path d="M0 1h2l1 5h6l1-4H3" stroke="#fff" fill="none"/><circle cx="4" cy="8.5" r="1" fill="#fff"/><circle cx="8" cy="8.5" r="1" fill="#fff"/></svg>My Shopping Cart (0)</div>

<section class="hero abs">
  <h2>Lorem ipsum dolor sit amet consectetur adipisicing elit</h2>
  <div class="art" role="img" aria-label="Stack of colourful books beside featured novel covers"></div>
  <div class="arrow-btn" style="left:2px"><svg viewBox="0 0 10 10"><path d="M7 2 3 5l4 3" stroke="#3a2a7a" fill="none" stroke-width="1.6"/></svg></div>
  <div class="arrow-btn" style="left:189px"><svg viewBox="0 0 10 10"><path d="M3 2l4 3-4 3" stroke="#3a2a7a" fill="none" stroke-width="1.6"/></svg></div>
  <div class="shop-now" style="left:155px;top:148px">SHOP NOW ▸</div>
</section>

<div class="promo abs" style="left:706px;top:55px;width:96px;height:75px">
  <div class="art" role="img" aria-label="Standing hardback book cover" style="left:5px;top:4px;width:44px;height:58px;background:linear-gradient(#c9b27a,#8a6d3b)"></div>
  <p style="left:56px;top:56px">Lorem ipsum dolor</p>
  <div class="strip"><span>STARTING $ 100</span><span class="btn">SHOP NOW ▸</span></div>
</div>
<div class="promo abs" style="left:706px;top:137px;width:96px;height:81px">
  <div class="art" role="img" aria-label="Dark fantasy novel cover" style="left:5px;top:4px;width:86px;height:64px;background:linear-gradient(135deg,#6b4a2a,#2b1d12)"></div>
  <div class="strip"><span>STARTING $ 100</span><span class="btn">SHOP NOW ▸</span></div>
</div>
<div class="promo abs" style="left:498px;top:224px;width:147px;height:65px">
  <div class="art" role="img" aria-label="Book stack with a novel cover" style="left:4px;top:3px;width:82px;height:50px;background:linear-gradient(90deg,#d65a8c,#3f9a6f)"></div>
  <p style="left:60px;top:2px;text-align:right;width:84px">Lorem ipsum dolor sit amet,<br>adipisicing elit,</p>
  <div class="shop-now" style="left:104px;top:42px">CLICK HERE</div>
  <div class="strip"><span>LEATHER BELT UP TO 50% OFF</span><span class="btn">SHOP NOW ▸</span></div>
</div>
<div class="promo abs" style="left:656px;top:224px;width:146px;height:65px">
  <div class="art" role="img" aria-label="Novel cover" style="left:18px;top:5px;width:30px;height:48px;background:linear-gradient(#5a7a4a,#2a3a22)"></div>
  <div class="badge" style="left:72px;top:22px"></div>
  <p style="left:86px;top:5px">Lorem ipsum dolor</p>
  <p style="left:111px;top:31px;color:#6a1a7a;font-weight:400">$34.00</p>
  <div class="shop-now" style="left:104px;top:42px">CLICK HERE</div>
  <div class="strip"><span>GARMENT UP TO 50% OFF</span><span class="btn">SHOP NOW ▸</span></div>
</div>

<form class="newsletter abs">
  <div class="label">Become our VIP and receive daily deals</div>
  <div class="field">Write your e_mail here to sing up to our news letter</div>
  <div class="btn">SIGN UP</div>
</form>

<!-- Top new releases -->
<h3 class="section-title abs" style="top:337px">Top New Releases in Books</h3>
<div class="nav-circle abs" style="left:367px;top:403px"><svg viewBox="0 0 19 19"><path d="M11 5 7 9.5l4 4.5" stroke="#fff" stroke-width="2" fill="none"/></svg></div>
<div class="nav-circle abs" style="left:812px;top:403px"><svg viewBox="0 0 19 19"><path d="M8 5l4 4.5L8 14" stroke="#fff" stroke-width="2" fill="none"/></svg></div>
<div class="shelf abs" style="top:355px">
  <article class="book"><div class="cover" role="img" aria-label="Book cover with a wading bird" style="background:linear-gradient(#9c8a5a,#5c4a2a)"></div><p class="title">Lorem ipsum dolor sit amet</p><div class="price"><s>$300</s><b>$280</b><em>10% Off</em></div><div class="cod"><svg viewBox="0 0 10 10"><path d="M0 1h2l1 5h6l1-4H3" stroke="#000" fill="none"/><circle cx="4" cy="8.5" r="1"/><circle cx="8" cy="8.5" r="1"/></svg>Cash on delivery available</div></article>
  <article class="book"><div class="cover" role="img" aria-label="Book cover with a domed monument" style="background:linear-gradient(#e8b84a,#3a5a8a)"></div><p class="title">Lorem ipsum dolor sit amet</p><div class="price"><s>$75</s><b>$280</b><em>10% Off</em></div><div class="cod"><svg viewBox="0 0 10 10"><path d="M0 1h2l1 5h6l1-4H3" stroke="#000" fill="none"/><circle cx="4" cy="8.5" r="1"/><circle cx="8" cy="8.5" r="1"/></svg>Cash on delivery available</div></article>
  <article class="book is-focus"><div class="cover" role="img" aria-label="Classic epic book cover" style="background:linear-gradient(#e0a050,#9a5a2a)"></div><p class="title">Lorem ipsum dolor sit amet</p><div class="price"><s>$300</s><b>$280</b><em>10% Off</em></div><div class="cod"><svg viewBox="0 0 10 10"><path d="M0 1h2l1 5h6l1-4H3" stroke="#000" fill="none"/><circle cx="4" cy="8.5" r="1"/><circle cx="8" cy="8.5" r="1"/></svg>Cash on delivery available</div></article>
  <article class="book"><div class="cover" role="img" aria-label="Illustrated memoir cover" style="background:linear-gradient(#f2f2ea,#5a7a4a)"></div><p class="title">Lorem ipsum dolor sit amet</p><div class="price"><s>$300</s><b>$280</b><em>10% Off</em></div><div class="cod"><svg viewBox="0 0 10 10"><path d="M0 1h2l1 5h6l1-4H3" stroke="#000" fill="none"/><circle cx="4" cy="8.5" r="1"/><circle cx="8" cy="8.5" r="1"/></svg>Cash on delivery available</div></article>
  <article class="book"><div class="cover" role="img" aria-label="Classic play cover" style="background:linear-gradient(#e6d4aa,#b0915a)"></div><p class="title">Lorem ipsum dolor sit amet</p><div class="price"><s>$300</s><b>$280</b><em>10% Off</em></div><div class="cod"><svg viewBox="0 0 10 10"><path d="M0 1h2l1 5h6l1-4H3" stroke="#000" fill="none"/><circle cx="4" cy="8.5" r="1"/><circle cx="8" cy="8.5" r="1"/></svg>Cash on delivery available</div></article>
</div>

<!-- Bestselling -->
<h3 class="section-title abs" style="top:487px">Bestselling Books at abcdef.com<span class="view-all">View all &nbsp;&gt;&gt;</span></h3>
<div class="shelf abs" style="top:504px">
  <article class="book"><div class="cover" role="img" aria-label="Book cover with a songbird" style="background:linear-gradient(#eef0e0,#8aa04a)"></div><p class="title">Lorem ipsum dolor sit amet</p><div class="price"><s>$300</s><b>$280</b><em>10% Off</em></div><div class="cod"><svg viewBox="0 0 10 10"><path d="M0 1h2l1 5h6l1-4H3" stroke="#000" fill="none"/><circle cx="4" cy="8.5" r="1"/><circle cx="8" cy="8.5" r="1"/></svg>Cash on delivery available</div></article>
  <article class="book"><div class="cover" role="img" aria-label="Dark novel cover" style="background:linear-gradient(#3a1a10,#a0301a)"></div><p class="title">Lorem ipsum dolor sit amet</p><div class="price"><s>$75</s><b>$280</b><em>10% Off</em></div><div class="cod"><svg viewBox="0 0 10 10"><path d="M0 1h2l1 5h6l1-4H3" stroke="#000" fill="none"/><circle cx="4" cy="8.5" r="1"/><circle cx="8" cy="8.5" r="1"/></svg>Cash on delivery available</div></article>
  <article class="book"><div class="cover" role="img" aria-label="Bird guide cover" style="background:linear-gradient(#f0e6a0,#8a8aa0)"></div><p class="title">Lorem ipsum dolor sit amet</p><div class="price"><s>$300</s><b>$280</b><em>10% Off</em></div><div class="cod"><svg viewBox="0 0 10 10"><path d="M0 1h2l1 5h6l1-4H3" stroke="#000" fill="none"/><circle cx="4" cy="8.5" r="1"/><circle cx="8" cy="8.5" r="1"/></svg>Cash on delivery available</div></article>
  <article class="book"><div class="cover" role="img" aria-label="Dark thriller cover" style="background:linear-gradient(#2a241a,#6a5030)"></div><p class="title">Lorem ipsum dolor sit amet</p><div class="price"><s>$300</s><b>$280</b><em>10% Off</em></div><div class="cod"><svg viewBox="0 0 10 10"><path d="M0 1h2l1 5h6l1-4H3" stroke="#000" fill="none"/><circle cx="4" cy="8.5" r="1"/><circle cx="8" cy="8.5" r="1"/></svg>Cash on delivery available</div></article>
  <article class="book"><div class="cover" role="img" aria-label="Novel cover with a butterfly" style="background:linear-gradient(#2a7a5a,#1a3a2a)"></div><p class="title">Lorem ipsum dolor sit amet</p><div class="price"><s>$300</s><b>$280</b><em>10% Off</em></div><div class="cod"><svg viewBox="0 0 10 10"><path d="M0 1h2l1 5h6l1-4H3" stroke="#000" fill="none"/><circle cx="4" cy="8.5" r="1"/><circle cx="8" cy="8.5" r="1"/></svg>Cash on delivery available</div></article>
</div>

<!-- Popular -->
<h3 class="section-title abs" style="top:636px">Popular books<span class="view-all">View all &nbsp;&gt;&gt;</span></h3>
<div class="shelf abs" style="top:654px">
  <article class="book"><div class="cover" role="img" aria-label="Fashion book cover" style="background:linear-gradient(#f4f4f4,#c8b8a0)"></div><p class="title">Lorem ipsum dolor sit amet</p><div class="price"><s>$300</s><b>$280</b><em>10% Off</em></div><div class="cod"><svg viewBox="0 0 10 10"><path d="M0 1h2l1 5h6l1-4H3" stroke="#000" fill="none"/><circle cx="4" cy="8.5" r="1"/><circle cx="8" cy="8.5" r="1"/></svg>Cash on delivery available</div></article>
  <article class="book"><div class="cover" role="img" aria-label="Science book cover" style="background:linear-gradient(#0a1a3a,#2a6aa0)"></div><p class="title">Lorem ipsum dolor sit amet</p><div class="price"><s>$75</s><b>$280</b><em>10% Off</em></div><div class="cod"><svg viewBox="0 0 10 10"><path d="M0 1h2l1 5h6l1-4H3" stroke="#000" fill="none"/><circle cx="4" cy="8.5" r="1"/><circle cx="8" cy="8.5" r="1"/></svg>Cash on delivery available</div></article>
  <article class="book"><div class="cover" role="img" aria-label="Animal encyclopedia cover" style="background:linear-gradient(#d08a3a,#7a4a1a)"></div><p class="title">Lorem ipsum dolor sit amet</p><div class="price"><s>$300</s><b>$280</b><em>10% Off</em></div><div class="cod"><svg viewBox="0 0 10 10"><path d="M0 1h2l1 5h6l1-4H3" stroke="#000" fill="none"/><circle cx="4" cy="8.5" r="1"/><circle cx="8" cy="8.5" r="1"/></svg>Cash on delivery available</div></article>
  <article class="book"><div class="cover" role="img" aria-label="Wildlife book cover" style="background:linear-gradient(#3a4a7a,#b07a3a)"></div><p class="title">Lorem ipsum dolor sit amet</p><div class="price"><s>$300</s><b>$280</b><em>10% Off</em></div><div class="cod"><svg viewBox="0 0 10 10"><path d="M0 1h2l1 5h6l1-4H3" stroke="#000" fill="none"/><circle cx="4" cy="8.5" r="1"/><circle cx="8" cy="8.5" r="1"/></svg>Cash on delivery available</div></article>
  <article class="book"><div class="cover" role="img" aria-label="Travel guide cover" style="background:linear-gradient(#2a6ad0,#6a9a4a)"></div><p class="title">Lorem ipsum dolor sit amet</p><div class="price"><s>$300</s><b>$280</b><em>10% Off</em></div><div class="cod"><svg viewBox="0 0 10 10"><path d="M0 1h2l1 5h6l1-4H3" stroke="#000" fill="none"/><circle cx="4" cy="8.5" r="1"/><circle cx="8" cy="8.5" r="1"/></svg>Cash on delivery available</div></article>
</div>

<!-- Publishers -->
<h3 class="section-title abs" style="top:781px;border:none">Our Company</h3>
<div class="publishers abs">
  <svg class="pub-arrow" style="left:4px" viewBox="0 0 10 14"><path d="M7 2 3 7l4 5" stroke="#555" fill="none" stroke-width="1.4"/></svg>
  <span class="publisher"><i></i>Quillhouse</span>
  <span class="publisher">Lanternleaf</span>
  <span class="publisher">Ferncliff</span>
  <span class="publisher"><i></i>Northpage</span>
  <span class="publisher">Wingset</span>
  <span class="publisher"><i></i></span>
  <svg class="pub-arrow" style="right:4px" viewBox="0 0 10 14"><path d="M3 2l4 5-4 5" stroke="#555" fill="none" stroke-width="1.4"/></svg>
</div>

<footer class="site-footer abs">
  <div class="col" style="left:53px"><h4>INFORMATION</h4>&gt; About Store<br>&gt; Contact Us<br>&gt; Customer Assitance<br>&gt; Privacy Policy<br>&gt; Terms &amp; Condition<br>&gt; Worldwide Delivery</div>
  <div class="col" style="left:156px"><h4>SHIPPING &amp; SUPPORT</h4>&gt; International Shipping<br>&gt; Orders and Returns<br>&gt; Delivery Information<br>&gt; Secure Shopping</div>
  <div class="col" style="left:263px"><h4>MY ACCOUNT</h4>&gt; My Account<br>&gt; Order History<br>&gt; Manufactures<br>&gt; New Collection<br>&gt; Wish List<br>&gt; Newsletter</div>
  <div class="col" style="left:358px;width:105px"><h4 style="padding-left:12px">CONTACT US</h4>
    <div class="contact-row" style="line-height:10px"><svg viewBox="0 0 8 8"><path d="M4 0a3 3 0 0 1 3 3c0 2-3 5-3 5S1 5 1 3a3 3 0 0 1 3-3z"/></svg>No 12 Harbor Lane 40/3 Millbrook City , NY United States</div>
    <div class="contact-row lnk"><svg viewBox="0 0 8 8"><rect y="1" width="8" height="6"/></svg>orders@pagewellbooks.com<br>orders@pagewellbooks.com</div>
    <div class="contact-row lnk"><svg viewBox="0 0 8 8"><path d="M1 1h2l1 2-1 1a4 4 0 0 0 2 2l1-1 2 1v2C3 8 0 5 1 1z"/></svg>(+40) 05550142-318<br>(+40) 05550142-318</div>
    <div class="social" style="padding-left:2px"><i></i><i></i><i></i><i style="background:#b22"></i></div>
  </div>
</footer>
<div class="to-top abs"><svg viewBox="0 0 23 23" width="23" height="23"><path d="M6 14l5.5-5.5L17 14" stroke="#fff" stroke-width="2.4" fill="none"/></svg></div>

<div class="legal abs">
  <span style="left:50px">Copyright 2013 abcdefgh.com All right reserved</span>
  <span style="right:50px">Delivery &amp; Returns &nbsp;|&nbsp; Terms &amp; conditions &nbsp;|Site Map| &nbsp;About Us</span>
</div>

</body>
</html>
```